Boracay Wedding Invitation Design

Hello, We would like a wedding invitation design for our wedding in Boracay. We would like it somewhat in the form of a boarding pass with beachy fresh colours, possibly a nice Boracay beach in the background Double sided with an envelope design to match. Maybe something simple on the envelope like a nice picture in the bottom left corner of a shell on a beach or something similar.

I would also like on the opposite side of the invite to be an "information sheet" with a matching beach design

The text files for both sides are included and i have also included 2 designs that i thought looked nice and are similar to what we are after.
Updates

Hello, I have updated the brief to be more specific with text files and images to make it easier for you. Thank you :)

Industry/Entity Type

Wedding

Font styles to use
Decorative
Script

Colors
fbee3d
33a6d7
33b8a4
fbf289
85cae6
ffffff

Requirements
Must have
• I would like to have this quote somewhere on the invitation
• This day I will marry my best friend,
• the one I laugh with,
• live for,
• dream with,
• love
• Owen & Marisa
• Request the pleasure of your company to celebrate their wedding
• On Friday the 17th March 2017
• at
• Velunda Grand Suites
• Boracay, Philippines
• Ceremony begins at 3.00pm
• RSVP
• Owen 0431907254
• Marisa 0417283649
• by
• 17th Jan 2016
• Dress: Beach Formal
• For the "information sheet"
• There will be a 5% discount on rooms booked at the Velunda under the event Owen & Marisa Wedding. The resort has a total of 24 rooms it would be nice if the majority of guests could stay at the resort from the night before until the night after the wedding but if you choose to stay elsewhere on the island there are plenty of other places to stay for cheaper and everything is fairly close as its a small island.
• We have currently blocked room stay for a short period of time so our guests can book rooms. If you choose to do so please email reservations@velundastays.example. Once rooms become available to the public again, towards the end of Jan, it will be first come first served basis. The resort is very popular so im assuming once this happens the rooms will be booked out.
• If you would like to check out the resort itself the website is www.velundagrand-isle.example
• We know its a fair distance to travel but we would really love to see you all there to celebrate and maybe even enjoy a small holiday while your here its a beautiful part of the world.
• If anyone has any questions please feel free to contact Owen on 0431907254
Nice to have
• A nice picture of a Boracay beach in the background would be nice

```html
<!DOCTYPE html>
<html lang="en">
<head>
<meta charset="utf-8">
<title>Owen &amp; Marisa – Wedding Invitation</title>
<link href="https://fonts.googleapis.com/css2?family=Amatic+SC:wght@400;700&family=Great+Vibes&family=Montserrat:wght@400;500&family=Open+Sans:wght@400;700&display=swap" rel="stylesheet">
<style>
  :root {
    --teal: #17b6c7;
    --teal-deep: #12a9bb;
    --teal-light: #72cbdb;
    --teal-veil: rgba(22, 182, 198, 0.72);
    --ink: #1d1d1d;
    --white: #ffffff;
    --line: #2a2a2a;
    --sky: #8fc7e8;
    --sea: #1fa3c4;
    --sand: #efe6d6;
  }
  * { box-sizing: border-box; margin: 0; padding: 0; }
  html, body { width: 1200px; height: 1000px; overflow: hidden; background: var(--white); }
  .canvas { position: relative; width: 1200px; height: 1000px; }

  .ticket {
    position: absolute; left: 80px; width: 993px; height: 373px;
    border: 1.5px solid var(--line); border-radius: 30px; overflow: hidden; background: var(--white);
  }
  .ticket--front { top: 96px; }
  .ticket--back { top: 532px; }

  .stub-title {
    position: absolute; left: 0; top: 0; width: 147px; height: 100%;
    display: flex; align-items: center; justify-content: center;
  }
  .stub-title span {
    writing-mode: vertical-rl; transform: rotate(180deg);
    font-family: "Amatic SC", cursive; font-weight: 700; font-size: 50px;
    letter-spacing: 1px; color: var(--teal); line-height: 1;
  }

  .beach-photo {
    position: absolute; left: 147px; top: 0; right: 0; bottom: 0;
    background: linear-gradient(180deg, #7fbfe6 0%, #b4d9ef 30%, #2aa6c6 40%, #3cc0cf 58%, #8fd3d6 72%, #d9d2bb 86%, #e9dfcb 100%);
  }
  .quote-wash {
    position: absolute; left: 720px; top: 0; right: 0; bottom: 0;
    background: linear-gradient(180deg, rgba(220,235,250,0.75) 0%, rgba(240,246,250,0.7) 55%, rgba(243,236,224,0.85) 100%);
  }
  .palm-deco {
    position: absolute;
    background: linear-gradient(160deg, rgba(140,215,228,0.55), rgba(140,215,228,0.15));
    border-radius: 40% 40% 10% 10%;
  }
  .palm-deco--front { left: 610px; top: 14px; width: 140px; height: 350px; }
  .palm-deco--back { left: 695px; top: 8px; width: 290px; height: 365px; background: linear-gradient(170deg, rgba(95,200,215,0.6), rgba(140,215,228,0.25)); }

  .name-band {
    position: absolute; left: 147px; top: 37px; width: 573px; height: 217px;
    background: var(--teal-veil);
  }
  .couple {
    position: absolute; left: 180px; top: 40px;
    font-family: "Great Vibes", cursive; font-size: 72px; color: var(--white); line-height: 1.2;
  }
  .invite-line {
    position: absolute; left: 182px; top: 180px; width: 400px;
    font-family: "Montserrat", sans-serif; font-size: 20px; line-height: 25px; color: var(--white);
  }

  .strip-light { position: absolute; left: 147px; right: 0; top: 254px; height: 16px; background: var(--teal-light); }
  .strip-main { position: absolute; left: 147px; right: 0; top: 270px; height: 52px; background: var(--teal-deep); }

  .date { position: absolute; left: 182px; top: 272px; font-family: "Open Sans", sans-serif; font-weight: 700; font-size: 20px; color: var(--white); }
  .venue { position: absolute; left: 182px; top: 303px; font-family: "Open Sans", sans-serif; font-size: 14px; color: var(--white); }
  .ceremony, .dress { position: absolute; left: 520px; font-family: "Open Sans", sans-serif; font-size: 12px; color: var(--white); }
  .ceremony { top: 281px; }
  .dress { top: 306px; }

  .quote {
    position: absolute; left: 755px; top: 32px; list-style: none;
    font-family: "Amatic SC", cursive; font-weight: 400; font-size: 24px; line-height: 31px; color: var(--teal);
  }
  .rsvp-label { position: absolute; left: 755px; top: 252px; font-family: "Montserrat", sans-serif; font-size: 12px; color: var(--white); }
  .rsvp-contacts { position: absolute; left: 755px; top: 268px; font-family: "Montserrat", sans-serif; font-size: 20px; line-height: 25px; color: var(--white); }
  .rsvp-by { position: absolute; left: 755px; top: 328px; font-family: "Montserrat", sans-serif; font-size: 19px; color: var(--teal); }

  .perforation { position: absolute; top: 0; bottom: 0; width: 0; border-left: 1.5px dashed; }
  .perforation--dark { border-color: #333; }
  .perforation--teal { border-color: var(--teal); }

  .info-sheet {
    position: absolute; left: 183px; top: 38px; width: 700px;
    font-family: "Montserrat", sans-serif; font-size: 12.2px; line-height: 16px; color: var(--ink);
  }
  .info-sheet p { margin-bottom: 27px; }
  .info-sheet p.spaced { margin-bottom: 29px; }
</style>
</head>
<body>
<main class="canvas">

  <section class="ticket ticket--front">
    <div class="stub-title"><span>Wedding Invitation</span></div>
    <div class="beach-photo" role="img" aria-label="Photograph of a tropical beach with blue sky, turquoise sea and white sand"></div>
    <div class="quote-wash"></div>
    <div class="name-band"></div>
    <div class="palm-deco palm-deco--front" role="img" aria-label="Translucent palm tree silhouettes and starfish illustration"></div>

    <h1 class="couple">Owen &amp; Marisa</h1>
    <p class="invite-line">Request the pleasure of your company to celebrate their wedding</p>

    <div class="strip-light"></div>
    <div class="strip-main"></div>
    <p class="date">On Friday the 17th March 2017</p>
    <p class="venue">at Velunda Grand Suites Boracay, Philippines</p>
    <p class="ceremony">Ceremony begins at 3.00pm</p>
    <p class="dress">Dress: Beach Formal</p>

    <ul class="quote">
      <li>This day I will marry</li>
      <li>my best friend,</li>
      <li>the one I laugh with,</li>
      <li>live for,</li>
      <li>dream with,</li>
      <li>love</li>
    </ul>
    <p class="rsvp-label">RSVP</p>
    <p class="rsvp-contacts">Owen 0431907254<br>Marisa 0417283649</p>
    <p class="rsvp-by">by 17th Jan 2016</p>

    <div class="perforation perforation--dark" style="left:146px"></div>
    <div class="perforation perforation--dark" style="left:715px"></div>
  </section>

  <section class="ticket ticket--back">
    <div class="palm-deco palm-deco--back" role="img" aria-label="Large translucent palm tree silhouettes"></div>
    <div class="perforation perforation--teal" style="left:146px"></div>
    <div class="perforation perforation--teal" style="left:715px"></div>
    <div class="info-sheet">
      <p>There will be a 5% discount on rooms booked at the Velunda under the event Owen &amp; Marisa Wedding. The resort has a total of 24 rooms it would be nice if the majority of guests could stay at the resort from the night before until the night after the wedding but if you choose to stay elsewhere on the island there are plenty of other places to stay for cheaper and everything is fairly close as its a small island.</p>
      <p>We have currently blocked room stay for a short period of time so our guests can book rooms. If you choose to do so please email reservations@velundastays.example. Once rooms become available to the public again, towards the end of Jan, it will be first come first served basis. The resort is very popular so im assuming once this happens the rooms will be booked out.</p>
      <p class="spaced">If you would like to check out the resort itself the website is:</p>
      <p>We know its a fair distance to travel but we would really love to see you all there to celebrate and maybe even enjoy a small holiday while your here its a beautiful part of the world.</p>
      <p>If anyone has any questions please feel free to contact Owen on 0431907254</p>
    </div>
  </section>

</main>
</body>
</html>
```